BRCW Business Cards

Business Cards should contain:
Bright Ridgecrest Coating Works
Felix Darrow
M: 0417 865 093
E: brightRCW@fernpost.example
BRCW logo
TCG logo
Painting & Decorating
Licence # 719362K
slogan: See The Shine Of Lasting Quality Work

Target Market(s)

all aspect of painting

Industry/Entity Type

Trade

Contact Information for Business Card

Felix Darrow
M: 0417 865 093
E: brightRCW@fernpost.example
BRCW logo
TCG logo
Painting & Decorating
Licence # 719362K

Font styles to use
Serif
Sans Serif

Requirements
Must have
• clear design with nice backround
• two sides
• smal TCG logo
Nice to have
• easy to read
Should not have
• mess
• black
• plastics form

```html
<!DOCTYPE html>
<html lang="en">
<head>
<meta charset="utf-8">
<title>BRCW Business Cards</title>
<link href="https://fonts.googleapis.com/css2?family=Alegreya:wght@500;700&family=Lato:wght@400;700&display=swap" rel="stylesheet">
<style>
  :root {
    --backdrop: #2a2928;
    --card-navy: #0e1f38;
    --card-white: #f4f4f3;
    --brand-teal: #1e5d5a;
    --brand-green: #4f8f38;
    --name-ink: #1b4a48;
    --badge-tone: #d9dde6;
    --serif: "Alegreya", Georgia, serif;
    --sans: "Lato", Arial, sans-serif;
  }
  html, body {
    margin: 0;
    padding: 0;
    width: 1200px;
    height: 1200px;
    overflow: hidden;
    background: var(--backdrop);
  }
  .canvas {
    position: relative;
    width: 1200px;
    height: 1200px;
  }
  .card {
    position: absolute;
    left: 115px;
    width: 970px;
    height: 540px;
    box-shadow: 0 6px 18px rgba(0,0,0,0.45);
  }
  .card--front { top: 40px; background: var(--card-navy); }
  .card--back { top: 620px; background: var(--card-white); }

  /* Front */
  .brand-mark {
    position: absolute;
    left: 318px;
    top: 240px;
    width: 90px;
    height: 90px;
    background: var(--brand-teal);
  }
  .brand-divider {
    position: absolute;
    left: 430px;
    top: 194px;
    width: 2px;
    height: 180px;
    background: var(--brand-teal);
  }
  .brand-initials {
    position: absolute;
    left: 446px;
    top: 200px;
    margin: 0;
    font-family: var(--serif);
    font-weight: 500;
    font-size: 82px;
    line-height: 1;
    letter-spacing: 1px;
    color: var(--brand-teal);
  }
  .brand-name {
    position: absolute;
    left: 448px;
    top: 292px;
    margin: 0;
    width: 300px;
    font-family: var(--serif);
    font-weight: 700;
    font-size: 29px;
    line-height: 39px;
    letter-spacing: -0.5px;
    color: var(--brand-green);
  }
  .brand-name span { display: block; }
  .slogan {
    position: absolute;
    left: 0;
    right: 0;
    top: 506px;
    margin: 0;
    text-align: center;
    padding-left: 40px;
    font-family: var(--sans);
    font-weight: 700;
    font-size: 26px;
    color: var(--brand-green);
  }

  /* Back */
  .person {
    position: absolute;
    right: 484px;
    top: 224px;
    text-align: right;
    font-family: var(--sans);
  }
  .person__name {
    margin: 0;
    font-weight: 700;
    font-size: 44px;
    line-height: 52px;
    color: var(--name-ink);
  }
  .person__role, .person__licence {
    margin: 0;
    font-size: 20px;
    line-height: 26px;
    color: var(--brand-green);
  }
  .contact-divider {
    position: absolute;
    left: 509px;
    top: 238px;
    width: 2px;
    height: 78px;
    background: var(--brand-green);
  }
  .contact-list {
    position: absolute;
    left: 537px;
    top: 242px;
    margin: 0;
    padding: 0;
    list-style: none;
    font-family: var(--sans);
    font-size: 23px;
    color: var(--brand-green);
  }
  .contact-list li {
    display: flex;
    align-items: center;
    height: 33px;
  }
  .contact-list svg {
    width: 26px;
    height: 26px;
    margin-right: 16px;
  }
  .association-badge {
    position: absolute;
    left: 793px;
    top: 400px;
    width: 160px;
    height: 112px;
    border-radius: 6px;
    background: var(--badge-tone);
  }
</style>
</head>
<body>
<div class="canvas">

  <section class="card card--front">
    <div class="brand-mark"></div>
    <div class="brand-divider"></div>
    <h1 class="brand-initials">BRCW</h1>
    <p class="brand-name">
      <span>Bright Ridgecrest</span>
      <span>Coating Works</span>
    </p>
    <p class="slogan">See The Shine Of Lasting Quality Work</p>
  </section>

  <section class="card card--back">
    <div class="person">
      <h2 class="person__name">Felix Darrow</h2>
      <p class="person__role">Painting &amp; Decorating</p>
      <p class="person__licence">Licence # 719362K</p>
    </div>
    <div class="contact-divider"></div>
    <ul class="contact-list">
      <li>
        <svg viewBox="0 0 26 26" aria-hidden="true">
          <rect x="8" y="3" width="10" height="20" rx="2" fill="none" stroke="#1b4a48" stroke-width="1.8"/>
          <circle cx="13" cy="19.5" r="1.2" fill="#1b4a48"/>
        </svg>
        <span>0417 865 093</span>
      </li>
      <li>
        <svg viewBox="0 0 26 26" aria-hidden="true">
          <rect x="2" y="6" width="22" height="15" fill="none" stroke="#1b4a48" stroke-width="1.6"/>
          <path d="M2 6 L13 15 L24 6 M2 21 L10 13 M24 21 L16 13" fill="none" stroke="#1b4a48" stroke-width="1.6"/>
        </svg>
        <span>brightRCW@fernpost.example</span>
      </li>
    </ul>
    <div class="association-badge"></div>
  </section>

</div>
</body>
</html>
```